Business cards and stationery for new company logo
TRV Enterprises
Business cards and stationery for new company logo - Construction
Creative Brief
Simple
Marcus Pellham
Owner
742 Wildrow Ave. Stittsville, Ontario K4T 2B5
marcus@trventerprises.ca
www.trventerprises.ca
Would like something sleek and corporate looking. Catchy. The logo that was designed has all those elements...I would like the bus cards and stationery to also have those.

```html
<!DOCTYPE html>
<html lang="en">
<head>
<meta charset="utf-8">
<title>TRV Enterprises – Business Cards</title>
<link rel="stylesheet" href="https://fonts.googleapis.com/css2?family=Arimo:wght@400;700&display=swap">
<style>
  :root {
    --backdrop: #dcdcdc;
    --card-white: #ffffff;
    --card-black: #0b0b0b;
    --brand-red: #d8232a;
    --ink: #1e1e1e;
    --ink-soft: #555555;
    --divider: #9a9a9a;
  }
  * { margin: 0; padding: 0; box-sizing: border-box; }
  html, body {
    width: 1200px; height: 871px; overflow: hidden;
    background: var(--backdrop);
    font-family: "Arimo", Arial, sans-serif;
  }
  .canvas { position: relative; width: 1200px; height: 871px; }

  .brand-wordmark {
    position: absolute; left: 690px; top: 110px; width: 470px;
    text-align: center;
  }
  .brand-wordmark .name {
    font-weight: 700; font-size: 62px; letter-spacing: 1px;
    color: var(--ink); line-height: 1.1;
  }

  .card {
    position: absolute; width: 580px; height: 340px;
    border-radius: 14px; overflow: hidden;
    box-shadow: 0 6px 18px rgba(0,0,0,0.25);
  }
  .card-front { left: 40px; top: 110px; background: var(--card-white); }
  .card-back {
    left: 580px; top: 470px; background: var(--card-black);
    display: flex; align-items: center; justify-content: center;
  }

  .card-front .front-logo {
    position: absolute; left: 34px; top: 122px; width: 230px;
    font-weight: 700; font-size: 30px; color: var(--ink); text-align: center;
  }
  .card-front .divider {
    position: absolute; left: 290px; top: 36px; width: 2px; height: 210px;
    background: var(--divider);
  }
  .contact { position: absolute; left: 310px; top: 38px; color: var(--ink-soft); font-size: 15px; line-height: 1.35; }
  .contact .person { color: var(--brand-red); font-size: 21px; font-weight: 700; }
  .contact .role { margin-bottom: 34px; }
  .contact .address { margin-bottom: 22px; }
  .contact .label { color: var(--brand-red); }

  .bottom-band {
    position: absolute; left: 0; right: 0; bottom: 0; height: 46px;
  }
  .bottom-band svg { display: block; }
  .web-address {
    position: absolute; right: 26px; bottom: 21px;
    color: #fff; font-size: 13px; font-weight: 700;
  }

  .card-back .back-logo {
    font-weight: 700; font-size: 58px; color: #ffffff;
  }
</style>
</head>
<body>
<main class="canvas">
  <div class="brand-wordmark"><div class="name">TRV Enterprises</div></div>

  <section class="card card-front">
    <div class="front-logo">TRV Enterprises</div>
    <div class="divider"></div>
    <div class="contact">
      <div class="person">Marcus Pellham</div>
      <div class="role">Owner</div>
      <div class="address">742 Wildrow Ave.<br>Stittsville, Ontario<br>K4T 2B5</div>
      <div><span class="label">C:</span> 613-555-0148</div>
      <div><span class="label">E:</span> marcus@trventerprises.ca</div>
    </div>
    <div class="bottom-band">
      <svg width="580" height="46" viewBox="0 0 580 46">
        <polygon points="0,22 580,22 580,46 0,46" fill="#111111"/>
        <polygon points="370,0 580,0 580,30 355,30" fill="#d8232a"/>
      </svg>
    </div>
    <div class="web-address">www.trventerprises.ca</div>
  </section>

  <section class="card card-back">
    <div class="back-logo">TRV Enterprises</div>
  </section>
</main>
</body>
</html>
```